A start up Private Wine Label for export to Asia.

We are looking for the best graphic design for our very first wine label Corvessa Vineyards and would like the following requirements:

1. Black background - explore and play around the shade of black
2. Gold Shimmery Colour Font
3. Font should be a cursive classic posh that says Corvessa Vineyards
4. We would like the front graphic design to be simple and elegant and has a traditional classic feel to it.

Target Market(s)

Small scale to test the upper class market for export to Asia

Font styles to use
Script

Colors

Designer to choose colors to be used in the design.

Requirements
Must have
• Gold font for the label Corvessa Vineyards with shimmery touch to it.
• Elegant black background.
• Simple but elegant design.
• Attractive to the upper class market in Asia.
Nice to have
• Explore and play around with your imagination.

```html
<!DOCTYPE html>
<html lang="en">
<head>
<meta charset="utf-8">
<title>Corvessa Vineyards – Shiraz 2019 Label</title>
<link rel="stylesheet" href="https://fonts.googleapis.com/css2?family=Pinyon+Script&family=Arimo&display=swap">
<style>
  :root {
    --black-deep: #050505;
    --black-soft: #2a2727;
    --gold-light: #f6e7a8;
    --gold-mid: #d6b258;
    --gold-dark: #b88f2f;
    --white: #ffffff;
  }
  * { margin: 0; padding: 0; box-sizing: border-box; }
  html, body {
    width: 1200px;
    height: 720px;
    overflow: hidden;
    background: var(--black-deep);
  }
  .label {
    position: relative;
    width: 1200px;
    height: 720px;
    overflow: hidden;
    background: radial-gradient(ellipse 60% 60% at 50% 40%, var(--black-soft) 0%, #141313 60%, var(--black-deep) 100%);
  }
  .label__frame {
    position: absolute;
    inset: 0;
  }
  .label__ornament {
    position: absolute;
    left: 150px;
    width: 900px;
    border-radius: 50%;
    background: radial-gradient(ellipse 50% 50% at 50% 50%, rgba(214,178,88,0.55) 0%, rgba(214,178,88,0.25) 55%, rgba(214,178,88,0) 100%);
  }
  .label__ornament--top { top: 72px; height: 96px; }
  .label__ornament--bottom { top: 428px; height: 92px; }
  .label__brand {
    position: absolute;
    left: 0;
    right: 0;
    top: 160px;
    text-align: center;
    font-family: "Pinyon Script", cursive;
    font-size: 132px;
    line-height: 1.2;
    white-space: nowrap;
    background: linear-gradient(180deg, var(--gold-dark) 0%, var(--gold-mid) 45%, var(--gold-light) 100%);
    -webkit-background-clip: text;
    background-clip: text;
    color: transparent;
  }
  .label__variety {
    position: absolute;
    left: 0;
    right: 0;
    top: 530px;
    text-align: center;
    font-family: "Pinyon Script", cursive;
    font-size: 56px;
    line-height: 1.2;
    color: var(--white);
  }
  .label__details {
    position: absolute;
    left: 0;
    right: 0;
    top: 662px;
    text-align: center;
    font-family: "Arimo", Arial, sans-serif;
    font-size: 15px;
    color: var(--white);
    word-spacing: 1px;
  }
  .label__band {
    position: absolute;
    left: 0;
    right: 0;
    top: 690px;
    height: 16px;
    background: linear-gradient(90deg, var(--gold-light), var(--gold-dark) 30%, var(--gold-mid) 60%, var(--gold-light));
  }
</style>
</head>
<body>
  <main class="label">
    <svg class="label__frame" width="1200" height="720" viewBox="0 0 1200 720" aria-hidden="true">
      <defs>
        <linearGradient id="frameGold" x1="0" y1="0" x2="1" y2="1">
          <stop offset="0" stop-color="#f6e7a8"/>
          <stop offset="0.35" stop-color="#b88f2f"/>
          <stop offset="0.7" stop-color="#d6b258"/>
          <stop offset="1" stop-color="#f6e7a8"/>
        </linearGradient>
      </defs>
      <path d="M94 48 L1106 48 A48 48 0 0 0 1154 96 L1154 592 A48 48 0 0 0 1106 640 L94 640 A48 48 0 0 0 46 592 L46 96 A48 48 0 0 0 94 48 Z"
            fill="none" stroke="url(#frameGold)" stroke-width="8"/>
    </svg>

    <div class="label__ornament label__ornament--top" role="img" aria-label="Gold baroque scroll flourish above the name"></div>

    <h1 class="label__brand">Corvessa Vineyards</h1>

    <div class="label__ornament label__ornament--bottom" role="img" aria-label="Gold baroque scroll flourish below the name"></div>

    <p class="label__variety">Shiraz 2019</p>

    <p class="label__details">ALC 12.0% BY VOL&nbsp;&nbsp;&nbsp;750ML</p>

    <div class="label__band"></div>
  </main>
</body>
</html>
```